Large scale additive manufacturing system brochure

Project Title: ZORIL Series THERMOPLASTIC EXTRUDER– Product Catalog Design

Description:
We need a professional catalog design for our ZORIL Series extruders (ZORIL15, ZORIL20, ZORIL32), which are high-performance extrusion systems for large-scale thermoplastic 3D printing. The catalog should highlight technical specifications, key features, applications, and company profile.

Requirements:
• Clean and modern layout aligned with Brimtel corporate colors
• 10–12 pages including cover, product comparison tables, technical details, and application visuals
• Output capacities should be presented based on PETG +30% GF benchmark
• Integration of company’s partnerships (TOLMI, OBRU, Qe Forge, Movrel)
• Space for product renders, real application images, and technical drawings
• English text will be provided, but layout and professional design are required

Deliverables:
• Editable source file (InDesign / Illustrator / similar)
• Print-ready PDF version

*i upload the previous catalog, which doesn’t show our vision abd future aim. We need a professional, unique and impressive design.

Target Market(s)

Defense, aerospace, marine, furniture, composite manufacturing

Industry/Entity Type

Robotics and automation

Font styles to use
Sans Serif

Colors

Designer to choose colors to be used in the design.

Requirements
Must have
• High tech impressive view
Nice to have
• Must seen a unique high tech product catalog

```html
<!DOCTYPE html>
<html lang="en">
<head>
<meta charset="utf-8">
<title>ZORIL Series – Materials &amp; Process Guidelines</title>
<link rel="stylesheet" href="https://fonts.googleapis.com/css2?family=Arimo:wght@400&family=Noto+Sans:wght@400&display=swap">
<style>
  :root {
    --sky-top: #9cc2da;
    --sky-mid: #6fa8c7;
    --sea-band: #3a88a9;
    --sky-bottom: #a3c5db;
    --ink: #0c0c0c;
    --header-orange: #dd8a30;
    --panel: rgba(112, 138, 168, 0.75);
    --cell-dark: #4a6b8b;
    --cell-mid: #5d7a98;
    --cell-light: #7089a7;
    --rule: #ffffff;
    --text-light: #ffffff;
  }
  * { margin: 0; padding: 0; box-sizing: border-box; }
  html, body { width: 848px; height: 1200px; overflow: hidden; }
  body {
    position: relative;
    font-family: "Arimo", Arial, sans-serif;
    color: var(--ink);
    background: linear-gradient(to bottom,
      var(--sky-top) 0%, #8cb8d3 30%, var(--sky-mid) 44%,
      var(--sea-band) 53%, #5c9cbd 62%, #8fbad5 75%, var(--sky-bottom) 100%);
  }
  .page-title {
    position: absolute; left: 57px; top: 34px;
    font-size: 34px; font-weight: 400; letter-spacing: 0.2px; white-space: nowrap;
  }
  .page-title small { font-size: 24px; }
  .intro {
    position: absolute; left: 57px; top: 75px; width: 730px;
    font-size: 19.6px; line-height: 24px;
  }
  .panel { position: absolute; background: var(--panel); }
  .panel-process { left: 48px; top: 152px; width: 765px; height: 346px; }
  .panel-materials { left: 23px; top: 601px; width: 797px; height: 523px; }
  table { position: absolute; border-collapse: collapse; table-layout: fixed; }
  th, td { border: 1.5px solid var(--rule); color: var(--text-light); font-weight: 400; }
  th { background: var(--header-orange); text-align: center; line-height: 1.2; }
  td { text-align: center; }
  .process-table { left: 57px; top: 162px; width: 746px; }
  .process-table th { height: 52px; font-size: 19px; }
  .process-table td { font-size: 16.5px; line-height: 1.25; }
  .process-table td.note { text-align: left; padding-left: 10px; padding-right: 4px; font-size: 17px; line-height: 20.5px; }
  .process-table tr.row-1 td { height: 100px; background: var(--cell-dark); }
  .process-table tr.row-2 td { height: 87px; background: var(--cell-mid); }
  .process-table tr.row-3 td { height: 87px; background: var(--cell-light); }
  .materials-table { left: 30px; top: 609px; width: 782px; }
  .materials-table th { height: 69px; font-size: 18px; }
  .materials-table td { height: 53px; font-size: 15.5px; font-family: "Noto Sans", Verdana, sans-serif; letter-spacing: 0.6px; }
  .materials-table td.mat { font-family: "Arimo", Arial, sans-serif; font-size: 16.5px; letter-spacing: 0; }
  .materials-table td.note { text-align: left; padding-left: 9px; padding-right: 4px; font-size: 16.5px; line-height: 20.5px; }
  .materials-table tr.tall td { height: 66px; }
  .materials-table tr.r-a td { background: #6a86a4; font-family: "Arimo", Arial, sans-serif; letter-spacing: 0; }
  .materials-table tr.r-b td { background: #48698a; font-family: "Arimo", Arial, sans-serif; letter-spacing: 0; }
  .materials-table tr.r-c td { background: #4c6d8e; }
  .materials-table tr.r-d td { background: #526f8e; }
  .materials-table tr.r-e td { background: #5a7694; }
  .materials-table tr.r-f td { background: #617b98; }
  .materials-table tr.r-g td { background: #68819d; }
  .materials-table tr.r-h td { background: #6f87a3; }
  .showcase-glow { position: absolute; left: 110px; top: 500px; width: 640px; height: 100px;
    background: radial-gradient(ellipse at center, rgba(150,215,240,0.45), rgba(150,215,240,0) 70%); }
  .piece { position: absolute; border-radius: 14px; }
  .piece-chair-orange { left: 134px; top: 506px; width: 141px; height: 88px;
    background: linear-gradient(120deg, #f5a24a, #f4e4d2 50%, #e88730); }
  .piece-panel-bronze { left: 295px; top: 503px; width: 92px; height: 93px; border-radius: 6px 36px 4px 4px;
    background: linear-gradient(to right, #5c5548, #857a66 60%, #6c624f); }
  .piece-chairs-grey { left: 397px; top: 503px; width: 166px; height: 93px;
    background: linear-gradient(160deg, #5a5a5c, #2e2f31 60%, #4a4b4d); }
  .piece-lounge-black { left: 578px; top: 504px; width: 146px; height: 92px; border-radius: 22px;
    background: linear-gradient(170deg, #2c333a, #12161b); }
</style>
</head>
<body>
  <h1 class="page-title">MATERIALS &amp; PROCESS GUIDELINES <small>(TYPICAL)</small></h1>
  <p class="intro">The following ranges are indicative; exact parameters depend on polymer grade, filler percentage, and part geometry. Benchmarking and tuning are recommended for each application.</p>

  <div class="panel panel-process"></div>
  <table class="process-table">
    <colgroup><col style="width:127px"><col style="width:146px"><col style="width:169px"><col style="width:115px"><col style="width:189px"></colgroup>
    <thead>
      <tr><th>Material</th><th>Typical Nozzle<br>Ø</th><th>Layer Height<br>Guideline</th><th>Melt Temp<br>Window</th><th>Notes</th></tr>
    </thead>
    <tbody>
      <tr class="row-1"><td>PETG +30%<br>GF (reference)</td><td>1.5-6.0 mm</td><td>30-60% of nozzle Ø</td><td>250-300 °C</td><td class="note">Reference material<br>for ZORIL throughput;<br>good dimensional<br>stability.</td></tr>
      <tr class="row-2"><td>PP +20-30%<br>GF</td><td>1.5-6.0 mm</td><td>30-60% of nozzle Ø</td><td>220-260 °C</td><td class="note">Lightweight<br>with chemical<br>resistance; shrinkage<br>management required.</td></tr>
      <tr class="row-3"><td>PA6/PA12 +<br>GF/CF</td><td>1.5-6.0 mm</td><td>30-50% of nozzle Ø</td><td>260-320 °C</td><td class="note">High strength;<br>moisture control<br>and enclosure<br>recommended.</td></tr>
    </tbody>
  </table>

  <div class="showcase-glow"></div>
  <div class="piece piece-chair-orange" role="img" aria-label="Photo of a 3D printed lounge chair with orange and white stripes"></div>
  <div class="piece piece-panel-bronze" role="img" aria-label="Photo of a large printed bronze-toned curved panel"></div>
  <div class="piece piece-chairs-grey" role="img" aria-label="Photo of a set of grey sculptural printed chairs around a petal-shaped table"></div>
  <div class="piece piece-lounge-black" role="img" aria-label="Photo of a black 3D printed lounge seat"></div>

  <div class="panel panel-materials"></div>
  <table class="materials-table">
    <colgroup><col style="width:91px"><col style="width:114px"><col style="width:92px"><col style="width:110px"><col style="width:108px"><col style="width:267px"></colgroup>
    <thead>
      <tr><th>Material</th><th>Nozzle<br>temperature<br>range</th><th>Stiffness<br>of the<br>material</th><th>Maximum<br>tensile<br>stress</th><th>Material<br>density</th><th>Notes</th></tr>
    </thead>
    <tbody>
      <tr class="r-a"><td class="mat">PLA</td><td>190-220 °C</td><td>3.5 GPa</td><td>50-70 MPa</td><td>1.24 g/cm³</td><td class="note">ParagBiodegrdable and easy to<br>print with low warping</td></tr>
      <tr class="r-b"><td class="mat">PC</td><td>260-310 °C</td><td>2.4 GPa</td><td>60-70 MPa</td><td>1.20 g/cm³</td><td class="note">High impact and temperature<br>resistance, transparent</td></tr>
      <tr class="r-c"><td class="mat">ABS</td><td>230–260 °C</td><td>2.1 GPa</td><td>40–50 MPa</td><td>1.04 g/cm³</td><td class="note">Durable, suitable for post<br>processing, large prints</td></tr>
      <tr class="r-d"><td class="mat">PA</td><td>240–270 °C</td><td>2.5 GPa</td><td>75–85 MPa</td><td>1.14 g/cm³</td><td class="note">Flexible and strong, with<br>high abrasion resistance</td></tr>
      <tr class="r-e tall"><td class="mat">TPU</td><td>220–250 °C</td><td>0.02 GPa</td><td>30–50 MPa</td><td>1.21 g/cm³</td><td class="note">Elastic, highly impact<br>resistant, suitable for flexible<br>parts</td></tr>
      <tr class="r-f"><td class="mat">PESU</td><td>370–430 °C</td><td>2.7 GPa</td><td>85–95 MPa</td><td>1.37 g/cm³</td><td class="note">Excellent chemical and heat<br>resistance for high-end uses</td></tr>
      <tr class="r-g"><td class="mat">PP</td><td>230–250 °C</td><td>2.1 GPa</td><td>45–55 MPa</td><td>1.27 g/cm³</td><td class="note">Tough, semi transparent,<br>and low shrinkage material</td></tr>
      <tr class="r-h"><td class="mat">PETG</td><td>230–250 °C</td><td>2.1 GPa</td><td>45–55 MPa</td><td>1.27 g/cm³</td><td class="note">Tough, semi-transparent and<br>low shrinkage material</td></tr>
    </tbody>
  </table>
</body>
</html>
```